Brix2Key Header

I want a professional Letterhead for my law firm. I'm attaching the letterhead I currently use in Word and PDF form. I'm also attaching my logo, and an example header that I like.

```html
<!DOCTYPE html>
<html lang="en">
<head>
<meta charset="utf-8">
<title>Brix2Key Letterhead</title>
<link rel="stylesheet" href="https://fonts.googleapis.com/css2?family=Tinos:wght@400;700&display=swap">
<style>
  :root {
    --ink: #333436;
    --charcoal: #333436;
    --sky: #02b7e6;
    --leaf: #58874d;
    --paper: #ffffff;
  }
  html, body {
    margin: 0;
    padding: 0;
    overflow: hidden;
    background: var(--paper);
  }
  .letterhead {
    position: relative;
    width: 849px;
    height: 1200px;
    background: var(--paper);
    overflow: hidden;
    font-family: "Tinos", "Times New Roman", serif;
    color: var(--ink);
  }
  .header-shapes,
  .footer-shapes {
    position: absolute;
    left: 0;
    display: block;
  }
  .header-shapes { top: 0; }
  .footer-shapes { top: 1151px; }
  .firm-name {
    position: absolute;
    left: 36px;
    top: 44px;
    margin: 0;
    font-family: "Tinos", "Times New Roman", serif;
    font-weight: 700;
    font-size: 58px;
    line-height: 1;
    letter-spacing: 1px;
    color: var(--paper);
  }
  .contact-block {
    position: absolute;
    right: 33px;
    top: 13px;
    margin: 0;
    text-align: right;
    font-size: 12.6px;
    line-height: 16.3px;
    text-transform: uppercase;
    color: var(--ink);
  }
  .contact-block span { display: block; }
</style>
</head>
<body>
<div class="letterhead">
  <svg class="header-shapes" width="849" height="152" viewBox="0 0 849 152" aria-hidden="true">
    <polygon points="0,0 400,0 508,141 0,141" fill="var(--charcoal)"/>
    <polygon points="408,0 416,0 524,141 515,141" fill="var(--sky)"/>
    <rect x="0" y="146" width="849" height="4.5" fill="var(--charcoal)"/>
  </svg>

  <h1 class="firm-name">BRIX2KEY</h1>

  <address class="contact-block">
    <span>Brixton K. Mercer III, Attorney at Law, PLLC</span>
    <span>2210 Lantern Avenue Suite 100</span>
    <span>Dallas, Texas 75299</span>
    <span>Telephone: (877) 555-0142</span>
    <span>Fax: (469) 555-0187</span>
    <span>Key@Brix2Key.net</span>
    <span>www.Brix2Key.com</span>
  </address>

  <svg class="footer-shapes" width="849" height="49" viewBox="0 0 849 49" aria-hidden="true">
    <polygon points="0,0 469,0 510,35 849,35 849,49 0,49" fill="var(--charcoal)"/>
    <polygon points="475,0 849,0 849,14 489,14" fill="var(--sky)"/>
    <polygon points="494,18 849,18 849,32 508,32" fill="var(--leaf)"/>
  </svg>
</div>
</body>
</html>
```